1 Page Bio, describing our Mission to buy multifamily properties in Colorado Springs.

I am uploading a sample of an associate who is doing a similar thing in Tampa Florida. I will also upload an attempt by my assistant to make the flyer and I will upload 3 pictures to use, along with another document that has text to add. I want to be able to edit the document pretty easily inside a google doc. thanks, I want it to look clean and professional.

```html
<!DOCTYPE html>
<html lang="en">
<head>
<meta charset="utf-8">
<title>Mission Flyer – Multifamily Residences, Colorado Springs</title>
<link rel="stylesheet" href="https://fonts.googleapis.com/css2?family=Lato:ital,wght@0,400;0,700;0,900;1,400;1,700&display=swap">
<style>
  :root {
    --stage: #1d2a1d;
    --green-deep: #17503f;
    --green-mid: #1d6e4c;
    --green-bright: #22a25a;
    --gold: #b97a2e;
    --gold-light: #d19a4a;
    --white: #ffffff;
    --paper: #f3f4f4;
    --panel: #d8dadb;
    --ink: #2f3534;
    --strip: #c9cbcc;
  }
  * { box-sizing: border-box; margin: 0; padding: 0; }
  html, body { width: 1200px; height: 1015px; overflow: hidden; }
  body {
    background: var(--stage);
    font-family: "Lato", Arial, sans-serif;
    position: relative;
  }
  .flyer {
    position: absolute;
    left: 220px; top: 15px;
    width: 760px; height: 985px;
    background: linear-gradient(150deg, var(--green-deep) 0%, var(--green-deep) 45%, var(--green-mid) 70%, var(--green-bright) 100%);
    overflow: hidden;
    color: var(--white);
  }
  .header-art { position: absolute; left: 0; top: 0; width: 760px; height: 312px; }
  .mission { position: absolute; left: 52px; top: 42px; }
  .mission-title { font-weight: 900; font-size: 31px; letter-spacing: .2px; }
  .mission-text { font-style: italic; font-size: 24px; line-height: 1.22; margin-top: 4px; }
  .promise {
    position: absolute; right: 38px; top: 196px; width: 430px;
    text-align: right; font-style: italic; font-weight: 700;
    color: var(--ink); font-size: 17px; line-height: 1.3;
  }
  .process {
    position: absolute; left: 0; top: 270px; width: 760px; height: 42px;
    background: linear-gradient(90deg, var(--gold) 0%, var(--gold-light) 50%, var(--gold) 100%);
    font-style: italic; font-weight: 700; font-size: 19px;
    padding: 9px 0 0 108px;
  }
  .column-left { position: absolute; left: 40px; top: 338px; width: 330px; }
  .section-title { font-weight: 700; font-size: 20px; line-height: 1.2; }
  .section + .section { margin-top: 24px; }
  .bullets { list-style: none; margin-top: 10px; font-size: 13.5px; line-height: 1.35; }
  .bullets li { position: relative; padding-left: 14px; }
  .bullets li::before { content: ""; position: absolute; left: 0; top: 7px; width: 5px; height: 5px; border-radius: 50%; background: var(--white); }
  .section p { margin-top: 10px; font-size: 13.5px; line-height: 1.35; }
  .headshots { position: absolute; left: 52px; top: 772px; display: flex; gap: 22px; }
  .headshot { width: 122px; text-align: center; font-size: 13.5px; font-weight: 700; }
  .headshot-photo {
    width: 122px; height: 128px; border: 4px solid var(--white);
    background: linear-gradient(180deg, #d7d7d7, #8e8e8e);
    margin-bottom: 6px;
  }
  .bio-panel {
    position: absolute; left: 400px; top: 312px; width: 340px; height: 470px;
    background: var(--panel);
    border-radius: 0 0 46px 46px;
    color: var(--ink);
    padding: 40px 22px 0 22px;
  }
  .bio-name { font-weight: 700; font-size: 19px; letter-spacing: .5px; }
  .bio-panel .bullets { font-size: 12.5px; margin-top: 12px; }
  .bio-panel .bullets li::before { background: var(--ink); }
  .bio-photo {
    position: absolute; left: 412px; top: 640px; width: 316px; height: 196px;
    border: 5px solid var(--white);
    background: linear-gradient(160deg, #7d8a6c 0%, #5c6752 45%, #a9a9a2 100%);
  }
  .contact {
    position: absolute; right: 40px; top: 862px;
    text-align: right; font-weight: 900; font-size: 19px; line-height: 1.3;
  }
  .bottom-strip { position: absolute; left: 0; bottom: 0; width: 760px; height: 22px; background: var(--strip); }
</style>
</head>
<body>
  <main class="flyer">
    <svg class="header-art" viewBox="0 0 760 312" aria-hidden="true">
      <defs>
        <linearGradient id="headerGreen" x1="0" y1="0" x2="0" y2="1">
          <stop offset="0" stop-color="#17503f"/>
          <stop offset="1" stop-color="#2cb060"/>
        </linearGradient>
      </defs>
      <rect width="760" height="312" fill="url(#headerGreen)"/>
      <path d="M0 238 C 200 250, 420 200, 760 150 L760 272 L0 272 Z" fill="#d19a4a"/>
      <path d="M0 250 C 210 258, 430 212, 760 164 L760 272 L0 272 Z" fill="var(--paper)"/>
      <path d="M560 210 C 640 190, 710 172, 760 164 L760 232 C 700 200, 640 198, 560 210 Z" fill="#bfe3cc" opacity=".6"/>
    </svg>

    <header class="mission">
      <h1 class="mission-title">The Mission:</h1>
      <p class="mission-text">To create a family business by purchasing<br>Multifamily Residences,<br>one at a time.</p>
    </header>

    <p class="promise">To provide a white<br>glove experience to all residences with a<br>clean, safe, and fun environment.</p>

    <div class="process">The Process : Buy right, manage right, and finance right</div>

    <section class="column-left">
      <div class="section">
        <h2 class="section-title">The Market:<br>Colorado Springs</h2>
        <ul class="bullets">
          <li>Projected job growth of nearly 50%</li>
          <li>Below average unemployment rates.</li>
          <li>Above-average incomes.</li>
          <li>Solid economy, military, aerospace, electronics industry, and tourism.</li>
        </ul>
      </div>
      <div class="section">
        <h2 class="section-title">The Target :</h2>
        <p>B and C class assets located in Colorado Springs or nearby submarkets.</p>
      </div>
      <div class="section">
        <h2 class="section-title">Curtis Hale</h2>
        <ul class="bullets">
          <li>Retired Electrical Engineer.</li>
          <li>Active Real Estate Investor/Consultant.</li>
          <li>Net worth over $4M</li>
          <li>15 Grandchildren.</li>
        </ul>
      </div>
    </section>

    <div class="headshots">
      <figure class="headshot">
        <div class="headshot-photo" role="img" aria-label="Portrait photo of Ben Ashby"></div>
        <figcaption>Ben Ashby</figcaption>
      </figure>
      <figure class="headshot">
        <div class="headshot-photo" role="img" aria-label="Portrait photo of Dale Norris"></div>
        <figcaption>Dale Norris</figcaption>
      </figure>
    </div>

    <aside class="bio-panel">
      <h2 class="bio-name">ROWAN HALE</h2>
      <ul class="bullets">
        <li>Licensed Colorado Real Estate Agent 18 years.</li>
        <li>Broker-Owner of two Summit Realty Franchises 7 and 2 Years.</li>
        <li>Real Estate investing for 5 years.</li>
        <li>Member of Keystone Investor Academy.</li>
        <li>Married 24 years to Elaine, parenting 10 children together.</li>
        <li>Appeared on The Rental Roundtable podcast Episode 43</li>
        <li>$2M portfolio.</li>
      </ul>
    </aside>

    <div class="bio-photo" role="img" aria-label="Outdoor photo of Rowan and Curtis Hale standing together"></div>

    <footer class="contact">
      Contact:<br>
      Rowan &amp; Curtis Hale 719-555-0142<br>
      rhale.invest@example.com
    </footer>

    <div class="bottom-strip"></div>
  </main>
</body>
</html>
```